Cocktail Reception Invitation - For New Office Location

We are a residential property management, investment, and acquisition company and we have recently moved to a new corporate headquarters. We are hosting an event for current customers/vendors, as well as prospects, to show off the new office and enhance the legitimacy of our brand. The event will be a cocktail reception with heavy appetizers/hors d'oeuvres and a bar. We want the invitation to be professional, clean, and somewhat modern. Would be great if we could have it formatted for both electronic delivery AND print, but print is the priority. Thanks in advance for submitting! Photo of the new building attached - does not have to be on the invitation though.

Target Market(s)

Investors, Property Owners, Contractors

Industry/Entity Type

Real Estate

Requirements
Must have
• Must have placeholders for event date, time, location, RSVP, etc. Date is Thursday November 17th from 4-7:00 PM at 418 W Marlow St, Indianapolis, IN 46208. The invitees are a very professional group of people and the invitation should be classy and clean.
Nice to have
• Our colors are Navy Blue, Orange, and dark gray. Not required if it doesn't look good on the invite but it might be nice. I have included a photo of the new office if it makes sens to have it on the invitation.

```html
<!DOCTYPE html>
<html lang="en">
<head>
<meta charset="utf-8">
<title>Cocktail Reception Invitation</title>
<link rel="stylesheet" href="https://fonts.googleapis.com/css2?family=Poiret+One&display=swap">
<style>
  :root {
    --backdrop: #f3f1f1;
    --card: #ffffff;
    --ink: #111111;
    --ink-soft: #3a3a3a;
    --wine: #9c1a4a;
    --wine-pale: #f4dde6;
  }
  * { margin: 0; padding: 0; box-sizing: border-box; }
  html, body {
    width: 1200px;
    height: 952px;
    overflow: hidden;
    background: var(--backdrop);
  }
  .invitation {
    position: absolute;
    left: 40px;
    top: 90px;
    width: 1120px;
    height: 772px;
    background: var(--card);
    border: 3px solid var(--ink);
    font-family: "Poiret One", sans-serif;
    color: var(--ink);
  }
  .splash {
    position: absolute;
    display: block;
  }
  .splash--upper { left: 36px; top: 150px; width: 92px; height: 300px; }
  .splash--lower { left: 44px; top: 600px; width: 130px; height: 96px; }
  .event {
    position: absolute;
    left: 140px;
    right: 40px;
    top: 118px;
    text-align: center;
    text-transform: uppercase;
  }
  .event p { white-space: nowrap; }
  .event__host {
    font-size: 24px;
    line-height: 34px;
    letter-spacing: 1px;
    color: var(--ink-soft);
  }
  .event__title {
    margin-top: 10px;
    font-size: 38px;
    line-height: 48px;
    letter-spacing: 2px;
    color: var(--wine);
  }
  .event__details {
    margin-top: 34px;
    font-size: 46px;
    line-height: 59px;
    letter-spacing: -0.5px;
  }
  .event__extras {
    margin-top: 34px;
    font-size: 22px;
    line-height: 34px;
    letter-spacing: 1px;
    color: var(--ink-soft);
  }
  .event__rsvp { text-transform: none; }
</style>
</head>
<body>
  <main class="invitation">
    <svg class="splash splash--upper" viewBox="0 0 92 300" role="img" aria-label="Wine-coloured ink splatter decoration">
      <defs>
        <linearGradient id="splashTone" x1="0" y1="0" x2="0" y2="1">
          <stop offset="0%" stop-color="#9c1a4a"/>
          <stop offset="100%" stop-color="#f4dde6"/>
        </linearGradient>
      </defs>
      <rect x="0" y="0" width="92" height="300" rx="46" fill="url(#splashTone)"/>
    </svg>
    <svg class="splash splash--lower" viewBox="0 0 130 96" role="img" aria-label="Small wine-coloured ink splatter decoration">
      <rect x="0" y="0" width="130" height="96" rx="48" fill="#9c1a4a"/>
    </svg>

    <section class="event">
      <p class="event__host">Harbor Lane Property Group invites you to celebrate our new headquarters</p>
      <h1 class="event__title">A Cocktail Reception</h1>
      <div class="event__details">
        <p>Thursday November 17th from 4-7:00 PM</p>
        <p>at 418 W Marlow St,</p>
        <p>Indianapolis, IN 46208</p>
      </div>
      <div class="event__extras">
        <p>Heavy hors d'oeuvres &amp; open bar</p>
        <p class="event__rsvp">RSVP by November 10 · rsvp@harborlaneproperty.com</p>
      </div>
    </section>
  </main>
</body>
</html>
```